Fancy looking Inspection Postcard

Postcard needed for customers to inspect their product once it is delivered. We'll be giving them the steps for inspecting their product and to contact us if any issues arise. Would like to see something that sticks out but uses our company's colors. Would like to see creativity. Possibly utilizing the diamond steel background like we have in our logo.

Target Market(s)

Customers of our manufacturing shop

Industry/Entity Type

Manufacturing - metal wall art, custom products

Requirements
Must have
• our colors and logo
Nice to have
• get creative. i like creativity

```html
<!DOCTYPE html>
<html lang="en">
<head>
<meta charset="utf-8">
<title>Basalt Creek Fabrication – Inspection Postcard</title>
<link href="https://fonts.googleapis.com/css2?family=Alfa+Slab+One&family=Oswald:wght@500;600&family=Roboto+Condensed:wght@400;500&family=Lato:wght@400&display=swap" rel="stylesheet">
<style>
  :root{
    --green:#74a043;
    --green-text:#6f9d3d;
    --black:#0b0b0b;
    --white:#ffffff;
    --stage:#4d4d4d;
    --sky:#86a6c6;
    --star:#e8502a;
    --bullet:#f2e600;
    --ink:#222222;
  }
  *{box-sizing:border-box;margin:0;padding:0}
  html,body{width:825px;height:1200px;overflow:hidden;background:var(--stage)}
  .card{position:absolute;background:var(--white);overflow:hidden}
  .card--front{left:30px;top:44px;width:755px;height:527px}
  .card--back{left:39px;top:603px;width:737px;height:527px}
  .card svg.shapes{position:absolute;left:0;top:0}
  .abs{position:absolute}

  .slab{font-family:"Alfa Slab One",serif}
  .cond{font-family:"Oswald",sans-serif}

  /* front */
  .brand{left:34px;top:70px;width:150px;display:flex;align-items:center;gap:8px;
    font-family:"Alfa Slab One",serif;font-size:15px;line-height:1.15;color:var(--black)}
  .brand__mark{width:14px;height:14px;background:var(--green);flex:none}
  .site-url{right:40px;top:12px;font-size:21px;color:var(--white)}
  .headline{left:32px;color:var(--white);font-size:33px;line-height:1.27}
  .headline--ask{top:210px}
  .headline--review{top:268px}
  .contact-email{left:32px;top:366px;color:var(--white);font-size:21px;line-height:1.25}
  .call-line{left:26px;top:438px;font-size:31px;color:var(--black);font-weight:600;letter-spacing:.5px}
  .call-line span{color:var(--white)}
  .text-box{left:470px;top:408px;width:285px;text-align:center}
  .text-box__label{font-size:22px;color:var(--black);letter-spacing:1px}
  .text-box__number{font-size:40px;font-weight:600;color:var(--white);line-height:1.15}

  /* back */
  .steps{font-family:"Roboto Condensed",sans-serif;color:var(--white);font-size:13px;line-height:16px}
  .steps h3{font-weight:500;font-size:13px}
  .steps li{list-style:none;padding-left:8px;position:relative}
  .steps li::before{content:"";position:absolute;left:0;top:5px;width:6px;height:6px;border-radius:50%;background:var(--bullet)}
  .stamp{left:568px;top:30px;width:134px;height:134px;border:1.5px solid var(--ink)}
  .opinion-title{left:34px;top:232px;font-family:"Lato",sans-serif;font-size:16px;color:var(--green-text);letter-spacing:-.3px}
  .rating{font-family:"Lato",sans-serif;font-size:10px;color:var(--ink)}
  .rating__stars{position:absolute;top:260px;color:var(--star);font-size:12px;letter-spacing:1px;transform:translateX(-50%)}
  .rating__label{position:absolute;left:34px}
  .rating__box{position:absolute;width:34px;height:15px;border:1.3px solid var(--ink);border-radius:4px;transform:translateX(-50%)}
  .panel{border:1.5px solid var(--ink);border-radius:7px;font-family:"Lato",sans-serif;font-size:10px;color:var(--ink)}
  .comments{left:34px;top:372px;width:157px;height:119px;padding:9px 6px}
  .details{left:203px;top:372px;width:244px;height:119px;padding:10px 8px 0 9px}
  .details__row{display:flex;align-items:flex-end;height:18px}
  .details__row span{white-space:nowrap;margin-right:10px}
  .details__row i{flex:1;border-bottom:1px solid var(--ink);margin-bottom:3px}
  .address-line{left:543px;width:165px;border-top:1px solid var(--ink)}
  .back-contact{right:29px;top:419px;text-align:right;font-family:"Oswald",sans-serif;font-weight:500;font-size:19px;line-height:24px;color:var(--black)}
  .back-contact .green{color:var(--green-text)}
</style>
</head>
<body>

<section class="card card--front">
  <svg class="shapes" width="755" height="527" viewBox="0 0 755 527" aria-hidden="true">
    <defs>
      <linearGradient id="frontPhoto" x1="0" y1="0" x2="1" y2="0">
        <stop offset="0" stop-color="#74a043"/>
        <stop offset=".45" stop-color="#7aa05c"/>
        <stop offset=".75" stop-color="#7f9fa6"/>
        <stop offset="1" stop-color="#86a6c6"/>
      </linearGradient>
    </defs>
    <polygon points="358,45 755,45 755,357 480,357 350,484 0,484 0,196 180,196" fill="url(#frontPhoto)" role="img" aria-label="Photo of a steel building frame against the sky"/>
    <polygon points="441,0 755,0 755,46 400,46" fill="var(--black)"/>
    <polygon points="156,196 201,145 271,145 222,196" fill="var(--black)"/>
    <rect x="32" y="258" width="380" height="3" fill="var(--black)"/>
    <polygon points="0,362 316,362 271,431 0,431" fill="var(--black)"/>
    <polygon points="480,392 755,392 755,507 470,507 443,527 354,527" fill="var(--green)"/>
  </svg>

  <div class="abs brand"><span class="brand__mark"></span>Basalt Creek Fabrication</div>
  <div class="abs slab site-url">www.basaltfab.com</div>
  <h1 class="abs slab headline headline--ask">Did we do a good job?</h1>
  <h2 class="abs slab headline headline--review">If you think so, leave us<br>a review on ReviewHub?</h2>
  <p class="abs slab contact-email">Please let us know<br>hello@basaltfab.com</p>
  <p class="abs cond call-line">CALL US <span>555-014-2290</span></p>
  <div class="abs cond text-box">
    <p class="text-box__label">SHOOT US A TEXT</p>
    <p class="text-box__number">(555) 017-3861</p>
  </div>
</section>

<section class="card card--back">
  <svg class="shapes" width="737" height="527" viewBox="0 0 737 527" aria-hidden="true">
    <defs>
      <linearGradient id="backPhoto" x1="0" y1="0" x2="1" y2="0">
        <stop offset="0" stop-color="#7ea64f"/>
        <stop offset=".5" stop-color="#6f8a6a"/>
        <stop offset=".85" stop-color="#5e6e7c"/>
        <stop offset="1" stop-color="#c9d3e3"/>
      </linearGradient>
    </defs>
    <polygon points="0,0 442,0 533,194 0,194" fill="url(#backPhoto)" role="img" aria-label="Photo of a steel building frame under construction"/>
    <polygon points="0,194 533,194 533,202 0,202" fill="#2b2b2b"/>
  </svg>

  <div class="abs steps" style="left:27px;top:55px">
    <h3>Step 1.&nbsp; Inspect general shape</h3>
    <ul><li>Is it what you expected?</li><li>Is it bent, disoriented?</li></ul>
  </div>
  <div class="abs steps" style="left:27px;top:120px">
    <h3>Step 2.&nbsp; Inspect the welds if there are any</h3>
    <ul><li>Do they look clean?</li><li>Are there any gaps?</li></ul>
  </div>
  <div class="abs steps" style="left:271px;top:55px">
    <h3>Step 3.&nbsp; Inspect the finish</h3>
    <ul><li>Are there any areas not finished?</li><li>Are the colors what you expected?</li></ul>
  </div>
  <div class="abs steps" style="left:271px;top:120px">
    <h3>Step 4.&nbsp; Check for functionality</h3>
    <ul><li>Does it work the way you want it to</li><li>Is it what you expected?</li></ul>
  </div>

  <div class="abs stamp"></div>

  <p class="abs opinion-title">WE VALUE YOUR OPINION, THANK YOU FOR YOUR TIME</p>

  <div class="rating">
    <span class="rating__stars" style="left:181px">★★★★★</span>
    <span class="rating__stars" style="left:242px">★★★★</span>
    <span class="rating__stars" style="left:305px">★★★</span>
    <span class="rating__stars" style="left:368px">★★</span>
    <span class="rating__stars" style="left:430px">★</span>

    <span class="rating__label" style="top:283px">Frindliness of staff?</span>
    <span class="rating__label" style="top:302px">Quality of service?</span>
    <span class="rating__label" style="top:322px">Value for money?</span>
    <span class="rating__label" style="top:341px">Overall experience?</span>

    <span class="rating__box" style="left:181px;top:282px"></span><span class="rating__box" style="left:242px;top:282px"></span><span class="rating__box" style="left:305px;top:282px"></span><span class="rating__box" style="left:368px;top:282px"></span><span class="rating__box" style="left:430px;top:282px"></span>
    <span class="rating__box" style="left:181px;top:301px"></span><span class="rating__box" style="left:242px;top:301px"></span><span class="rating__box" style="left:305px;top:301px"></span><span class="rating__box" style="left:368px;top:301px"></span><span class="rating__box" style="left:430px;top:301px"></span>
    <span class="rating__box" style="left:181px;top:321px"></span><span class="rating__box" style="left:242px;top:321px"></span><span class="rating__box" style="left:305px;top:321px"></span><span class="rating__box" style="left:368px;top:321px"></span><span class="rating__box" style="left:430px;top:321px"></span>
    <span class="rating__box" style="left:181px;top:340px"></span><span class="rating__box" style="left:242px;top:340px"></span><span class="rating__box" style="left:305px;top:340px"></span><span class="rating__box" style="left:368px;top:340px"></span><span class="rating__box" style="left:430px;top:340px"></span>
  </div>

  <div class="abs panel comments">Any other comments?</div>
  <div class="abs panel details">
    <div class="details__row"><span>Name</span><i></i></div>
    <div class="details__row"><span>Signature</span><i></i></div>
    <div class="details__row"><span>Date</span><i></i></div>
    <div class="details__row"><span>Make/Model</span><i></i></div>
    <div class="details__row"><span>Registration No.</span><i></i></div>
    <div class="details__row"><span>Salesmans Name</span><i></i></div>
  </div>

  <div class="abs address-line" style="top:305px"></div>
  <div class="abs address-line" style="top:340px"></div>
  <div class="abs address-line" style="top:375px"></div>

  <div class="abs back-contact">
    <p>Please let us know</p>
    <p>hello@basaltfab.com</p>
    <p class="green">CALL US 555-014-2290</p>
  </div>
</section>

</body>
</html>
```